Need flyer for honey

I need the advertising flyer for my honey products. Will need around 4-6 page A5 size. Flyer content is ready but will need to check the wording and need the artwork and pictures designed in a proper manner.

Advertising

```html
<!DOCTYPE html>
<html lang="en">
<head>
<meta charset="utf-8">
<title>Why Australian Honey – Flyer</title>
<link href="https://fonts.googleapis.com/css2?family=Montserrat:wght@700;800&family=Great+Vibes&family=Roboto+Condensed:ital,wght@1,700&family=Lato:wght@400&family=Crimson+Text:wght@700&display=swap" rel="stylesheet">
<style>
  :root {
    --cream: #f5ecd3;
    --cream-deep: #e6d49e;
    --gold: #f2b51c;
    --gold-light: #fbdc6a;
    --amber: #d9731c;
    --brown: #8a3e1e;
    --silver: #d9d2c6;
    --ink: #1a1208;
    --text: #2a2218;
  }
  * { box-sizing: border-box; margin: 0; padding: 0; }
  html, body { width: 900px; height: 1200px; overflow: hidden; }
  body { background: #ffffff; }
  .flyer {
    position: relative;
    width: 900px; height: 1200px;
    overflow: hidden;
    background: radial-gradient(ellipse at 60% 55%, #fbf5e2 0%, var(--cream) 45%, var(--cream-deep) 100%);
    font-family: "Lato", sans-serif;
    color: var(--text);
  }
  .hero-photo {
    position: absolute; left: 0; top: 0; width: 900px; height: 330px;
    background: radial-gradient(ellipse at 30% 30%, #fff2a8 0%, var(--gold-light) 25%, var(--gold) 55%, #c98a10 100%);
  }
  .swoosh-top { position: absolute; left: 0; top: 170px; width: 900px; height: 260px; }
  .swoosh-bottom { position: absolute; left: 0; top: 880px; width: 900px; height: 320px; }
  .title {
    position: absolute; right: 38px; top: 245px; text-align: right;
  }
  .title-main {
    font-family: "Montserrat", sans-serif; font-weight: 800;
    font-size: 44px; color: var(--ink); letter-spacing: 0.5px; line-height: 1;
  }
  .title-script {
    font-family: "Great Vibes", cursive; font-size: 82px; color: var(--ink);
    line-height: 1; margin-top: 2px; margin-right: 40px;
  }
  .content { position: absolute; left: 0; top: 378px; width: 900px; }
  .section { margin-bottom: 6px; }
  .section-head {
    display: block; width: 430px; height: 34px;
    padding-left: 45px; line-height: 34px;
    background: linear-gradient(90deg, var(--amber) 0%, #f0a22a 55%, rgba(250,210,120,0) 100%);
    font-family: "Roboto Condensed", sans-serif; font-style: italic; font-weight: 700;
    font-size: 23px; color: var(--ink); text-transform: uppercase;
    margin-bottom: 8px;
  }
  .section p {
    font-size: 15.6px; line-height: 1.27; text-align: justify;
    padding: 0 42px 0 45px;
  }
  .section.narrow p { padding-right: 110px; }
  .section.narrower p { padding-right: 250px; text-align: left; }
  .jar-photo {
    position: absolute; left: 700px; top: 960px; width: 200px; height: 175px;
    border-radius: 40% 10% 10% 30%;
    background: radial-gradient(circle at 40% 55%, #e58b1f 0%, #c8651a 40%, #f1c978 75%, rgba(240,210,140,0) 100%);
  }
  .contact-band {
    position: absolute; left: 0; bottom: 0; width: 900px; height: 74px;
    display: flex; align-items: center; gap: 30px; padding-left: 45px;
    font-family: "Crimson Text", serif; font-weight: 700; color: var(--ink);
  }
  .contact-label { font-size: 23px; }
  .contact-phone { font-size: 19px; letter-spacing: 0.5px; }
</style>
</head>
<body>
<main class="flyer">
  <div class="hero-photo" role="img" aria-label="Close-up photo of golden honey with a drop splashing into it"></div>

  <svg class="swoosh-top" viewBox="0 0 900 260" preserveAspectRatio="none" aria-hidden="true">
    <defs>
      <linearGradient id="silverBand" x1="0" y1="0" x2="1" y2="0">
        <stop offset="0" stop-color="#f4efe6"/>
        <stop offset="0.5" stop-color="#cfc6b7"/>
        <stop offset="1" stop-color="#f7f2e8"/>
      </linearGradient>
      <linearGradient id="amberBand" x1="0" y1="0" x2="1" y2="0">
        <stop offset="0" stop-color="#f3a623"/>
        <stop offset="0.6" stop-color="#d8701c"/>
        <stop offset="1" stop-color="#8a3e1e"/>
      </linearGradient>
    </defs>
    <path d="M0 50 C 250 120, 520 90, 900 0 L 900 30 C 560 130, 300 150, 0 110 Z" fill="url(#amberBand)"/>
    <path d="M0 95 C 280 150, 560 120, 900 20 L 900 60 C 600 160, 320 200, 0 165 Z" fill="url(#silverBand)"/>
    <path d="M0 160 C 300 200, 600 160, 900 60 L 900 75 C 620 180, 300 230, 0 200 Z" fill="#e2962a"/>
    <path d="M0 200 C 300 235, 620 185, 900 75 L 900 260 L 0 260 Z" fill="var(--cream)" opacity="0.85"/>
  </svg>

  <header class="title">
    <h1 class="title-main">WHY AUSTRALIAN</h1>
    <div class="title-script">Honey?</div>
  </header>

  <section class="content">
    <article class="section">
      <h2 class="section-head">Clean &amp; Chemical Free</h2>
      <p>Unlike many other countries producing honey, Australia has miles of pristine native forests and diverse native flowers that are chemical free which provides the clean honey nectar resources. Meanwhile, the honey bee industry is well protected by the Australia Quarantine and Inspection Service which keeps industry free from varroa mite and other exotic diseases. Very rare the chemicals are used in diseases control. Therefore from the very original source, Australia honey is clean than from any other part of the world.</p>
    </article>
    <article class="section">
      <h2 class="section-head">Pure &amp; Healthy</h2>
      <p>Honey is healthy food, while many overseas honey producers are commercialized, who would minimize the honey production circle to enhance production and adulterate their honey to make it a common consistency. Color and flavor are controlled by adding additives, sugars, syrups and extenders.<br>On the other hand, the Australian honey bee industry has a commitment to purity. Australian honey producers do not use any of the additives or sugars to make their honey better looking. Instead, they insist to make honey that is 100% pure and natural. Honey is left in the hives to let bee fan it until the water content drops to a certain level while the nutrition level is protected and raised.</p>
    </article>
    <article class="section narrow">
      <h2 class="section-head">Unique Taste</h2>
      <p>Australia is home to more than ten thousand species of plants and flowers, many of which are found nowhere else in the world. The country's unique native Eucalyptus trees and flowers create distinctive flavors of honey. From dark amber to golden light in the color, Australia honey delivers various tastes from gentle sweetness and mild caramel like to noticeable fragrance and sweet. Out of which everyone can find a taste of his own.</p>
    </article>
    <article class="section narrower">
      <h2 class="section-head">Safety Assured</h2>
      <p>As a country prioritizes its people's health and safety, the Australia government and regulation bodies have established the world's most strict food safety standards. There are also strict quality control procedures in the honey &amp; bee industry that all apiarists and honey packers must adhere to. Therefore, Australia is the rare country in the world that has very low risk of contamination from honey collection to packing and to distribution.</p>
    </article>
  </section>

  <svg class="swoosh-bottom" viewBox="0 0 900 320" preserveAspectRatio="none" aria-hidden="true">
    <defs>
      <linearGradient id="silverBandLow" x1="0" y1="0" x2="1" y2="0">
        <stop offset="0" stop-color="#f2ece1"/>
        <stop offset="0.6" stop-color="#d3cabb"/>
        <stop offset="1" stop-color="#b9ae9c"/>
      </linearGradient>
      <linearGradient id="footerBand" x1="0" y1="0" x2="1" y2="0">
        <stop offset="0" stop-color="#d9731c"/>
        <stop offset="0.5" stop-color="#f2b51c"/>
        <stop offset="1" stop-color="#f7c640"/>
      </linearGradient>
    </defs>
    <path d="M900 0 C 800 120, 650 210, 0 245 L 0 255 C 660 225, 820 150, 900 40 Z" fill="#c7bba8"/>
    <path d="M900 40 C 820 160, 660 230, 0 255 L 0 320 L 900 320 Z" fill="url(#silverBandLow)"/>
    <path d="M0 262 C 300 262, 600 248, 900 222 L 900 320 L 0 320 Z" fill="url(#footerBand)"/>
  </svg>

  <div class="jar-photo" role="img" aria-label="Photo of a jar of honey with a wooden spoon and honeycomb pieces"></div>

  <footer class="contact-band">
    <span class="contact-label">Contact Us:</span>
    <span class="contact-phone">xxx-xxxx-xxx</span>
  </footer>
</main>
</body>
</html>
```